University of Carrowmere Lindell Saxophone Quartet Concert

We need a poster design advertising the Lindell Saxophone Quartet Concert on Tuesday, April 23 at 5pm. The program concert will consist of 2 works by Peter Voskuilen: Harbor Lanterns and Meridian ledger. These two works should be included on the poster being the concert is featuring the composer and his works. Peter Voskuilen is known for his very "natural" sounding music. He resides in Montana and writes mostly from his small cottage in the mountains. This same idea of nature and "Montana" should be included on the poster design. He is deeply influenced by Thrane and most of the music he writes is play offs from Thrane Chorales.

The concert title is: "Where Stillness Gathers Near"

Target Market(s)

Collegiate Musician, Professional Musicians, Music Faculty

Industry/Entity Type

Advertising

Requirements
Must have
• 1. Title of the Concert: "Where Stillness Gathers Near"
2. "Lindell Saxophone Quartet Presents"
3. Date (April 23)
4. Time: 5pm
5. Location: Chapel of The Gentle Osric
Nice to have
• Nice to maybe keep the idea of "Montana" and that mountian-esque feel

```html
<!DOCTYPE html>
<html lang="en">
<head>
<meta charset="utf-8">
<title>Where Stillness Gathers Near — Lindell Saxophone Quartet</title>
<link rel="stylesheet" href="https://fonts.googleapis.com/css2?family=Montserrat:wght@600;700;800;900&family=Rubik+Dirt&display=swap">
<style>
  :root {
    --sky-top: #b9cee6;
    --sky-low: #dbe3ee;
    --ridge: #8592b9;
    --snow: #d9dde9;
    --forest-deep: #1f3514;
    --forest: #3c5f22;
    --meadow-far: #6ea52a;
    --meadow: #86c037;
    --meadow-near: #7fb52e;
    --ink-white: #ffffff;
    --ink-faded: rgba(255, 255, 255, 0.55);
    --ink-slate: #9aa8ba;
    --ink-dark: #1b220e;
  }
  html, body {
    margin: 0;
    padding: 0;
    overflow: hidden;
    background: #ffffff;
  }
  .poster {
    position: relative;
    width: 900px;
    height: 1200px;
    overflow: hidden;
    font-family: "Montserrat", sans-serif;
  }
  .landscape {
    position: absolute;
    inset: 0;
    background: linear-gradient(
      to bottom,
      var(--sky-top) 0%,
      var(--sky-low) 25%,
      var(--snow) 28%,
      var(--ridge) 33%,
      var(--ridge) 39%,
      var(--forest) 42%,
      var(--forest-deep) 50%,
      var(--forest) 56%,
      var(--meadow-far) 60%,
      var(--meadow) 75%,
      var(--meadow-near) 100%
    );
  }
  .billing {
    position: absolute;
    left: 44px;
    top: 54px;
    color: var(--ink-white);
  }
  .billing__ensemble {
    margin: 0;
    font-size: 22px;
    font-weight: 800;
    letter-spacing: 0.4px;
    line-height: 1.1;
  }
  .billing__presents {
    margin: 2px 0 0;
    font-size: 18px;
    font-weight: 800;
    color: var(--ink-faded);
    letter-spacing: 0.4px;
  }
  .billing__composer {
    margin: 20px 0 0;
    font-size: 37px;
    font-weight: 800;
    letter-spacing: 1px;
    line-height: 1;
    text-shadow: 0 1px 3px rgba(0,0,0,0.25);
  }
  .billing__works {
    margin: 18px 0 0;
    padding-left: 94px;
    font-size: 21px;
    font-weight: 800;
    color: var(--ink-slate);
    line-height: 1.4;
    text-align: center;
    width: 300px;
  }
  .title {
    position: absolute;
    right: 22px;
    top: 6px;
    bottom: 18px;
    margin: 0;
    display: flex;
    flex-direction: column;
    justify-content: space-between;
    align-items: flex-end;
    font-family: "Rubik Dirt", sans-serif;
    font-weight: 400;
    font-size: 112px;
    line-height: 1;
    color: var(--ink-white);
    text-transform: uppercase;
    text-shadow: 0 2px 6px rgba(0,0,0,0.18);
  }
  .title__line--wide { margin-top: 210px; }
  .details {
    position: absolute;
    left: 44px;
    top: 1060px;
    color: var(--ink-dark);
  }
  .details__when {
    margin: 0;
    font-size: 41px;
    font-weight: 900;
    line-height: 1;
  }
  .details__venue {
    margin: 8px 0 0;
    font-size: 25px;
    font-weight: 800;
    font-variant: small-caps;
    line-height: 1;
  }
</style>
</head>
<body>
  <main class="poster">
    <div class="landscape" role="img" aria-label="Painted Montana landscape: snow-capped mountains over a pine forest and lake, with a small wooden cabin in a green meadow"></div>

    <header class="billing">
      <p class="billing__ensemble">LINDELL SAXOPHONE QUARTET</p>
      <p class="billing__presents">PRESENTS</p>
      <p class="billing__composer">PETER VOSKUILEN</p>
      <p class="billing__works">HARBOR LANTERNS<br>MERIDIAN LEDGER</p>
    </header>

    <h1 class="title">
      <span class="title__line">Where</span>
      <span class="title__line title__line--wide">Stillness</span>
      <span class="title__line">Gathers</span>
      <span class="title__line">Near</span>
    </h1>

    <footer class="details">
      <p class="details__when">APRIL 23 5PM</p>
      <p class="details__venue">Chapel of The Gentle Osric</p>
    </footer>
  </main>
</body>
</html>
```